Back Pain

Need a flyer similar to the attached draft. This is to be handed out to prospective patients. Note that Sketch Hive has already designed the logo. If you need a copy please contact me

```html
<!DOCTYPE html>
<html lang="en">
<head>
<meta charset="utf-8">
<title>Tech Neck – Spine Ease Clinic flyer</title>
<link rel="stylesheet" href="https://fonts.googleapis.com/css2?family=Open+Sans:wdth,wght@75..100,300..800&display=swap">
<style>
  :root{
    --page:#d8cbb2;
    --paper:#ffffff;
    --charcoal:#3b3b3d;
    --charcoal-soft:#4a4a4c;
    --blue:#2a86c9;
    --bar-blue:#4f86c6;
    --green:#66bb46;
    --purple:#8a86c0;
    --rose:#d46a72;
    --red:#cc343c;
    --grey-text:#6e6e70;
    --ink:#222;
  }
  *{box-sizing:border-box;margin:0;padding:0}
  html,body{width:1200px;height:898px;overflow:hidden;background:var(--page)}
  body{font-family:"Open Sans",Arial,sans-serif;position:relative}
  .flyer{position:absolute;left:296px;top:19px;width:608px;height:860px;background:var(--paper);overflow:hidden;box-shadow:0 2px 10px rgba(0,0,0,.12)}
  .layer{position:absolute;left:0;top:0}
  .brand{position:absolute;left:36px;top:58px;display:flex;align-items:center;gap:10px}
  .brand-dot{width:34px;height:34px;border-radius:50%;background:var(--blue)}
  .brand-name{font-weight:700;font-size:20px;color:var(--blue);letter-spacing:.2px}
  .brand-sub{position:absolute;left:80px;top:96px;font-size:9px;letter-spacing:1.6px;color:var(--green);font-weight:600}
  .contact{position:absolute;right:36px;top:24px;text-align:center;color:var(--grey-text);font-size:13px;line-height:17px;font-style:normal}
  .title{position:absolute;left:90px;top:154px;font-size:84px;font-weight:400;font-stretch:85%;color:var(--blue);letter-spacing:-1px;line-height:1}
  .photo{position:absolute;left:288px;top:252px;width:124px;height:350px;border-radius:50px 50px 8px 8px;background:linear-gradient(180deg,#5a5a5c 0%,#2b2b2d 60%,#1e1e20 100%)}
  .chart-caption{position:absolute;left:46px;top:312px;font-size:15px;line-height:17px;font-stretch:75%;color:var(--ink)}
  .axis-x{position:absolute;left:60px;top:604px;font-size:12px;font-stretch:75%;color:var(--ink)}
  .axis-y{position:absolute;left:172px;top:442px;width:180px;height:16px;line-height:16px;text-align:center;font-size:12px;font-stretch:75%;color:var(--ink);transform:rotate(-90deg);transform-origin:center}
  .care{position:absolute;left:330px;top:602px;width:262px;text-align:center;font-stretch:80%;line-height:21px;font-size:17px;color:#fff}
  .care-head{color:var(--blue);font-size:26px;font-weight:600;line-height:30px}
  .care-foot{color:var(--green);font-weight:700}
  .usage{position:absolute;left:28px;top:662px;width:250px;font-stretch:75%;color:#fff;font-size:14px;line-height:16px}
  .usage-em{color:var(--blue);font-weight:700;font-size:21px;line-height:22px}
  .offer{position:absolute;left:222px;top:734px;width:356px;height:48px;border-radius:14px;background:var(--blue);color:#fff;display:flex;align-items:baseline;padding:0 16px;gap:8px}
  .offer-big{font-size:46px;font-weight:400;line-height:48px}
  .offer-small{font-size:17px}
  .booking{position:absolute;left:222px;top:790px;width:356px;text-align:center;font-size:15px;line-height:20px;color:var(--ink)}
  .booking-url{color:var(--green);font-weight:700;font-size:16px}
</style>
</head>
<body>
<main class="flyer">
  <svg class="layer" width="608" height="860" viewBox="0 0 608 860" aria-hidden="true">
    <rect class="header-band" x="0" y="0" width="608" height="150" fill="var(--charcoal)"/>
    <path class="info-band" d="M0,648 Q300,618 608,560 L608,700 Q300,752 0,822 Z" fill="var(--charcoal-soft)"/>
  </svg>

  <div class="brand"><span class="brand-dot"></span><span class="brand-name">SPINE EASE CLINIC</span></div>
  <div class="brand-sub">DR DAN MARSH - CHIROPRACTOR</div>

  <address class="contact">
    Dr Daniel Marsh<br>Now at<br>42 Harbour Rd - Quay Suites<br>Bayview WA 6200<br>T 0400 000 123
  </address>

  <h1 class="title">TECH NECK</h1>

  <div class="photo" role="img" aria-label="Photo of a man in a shirt and vest looking down at his phone, holding a bag"></div>

  <svg class="layer" width="608" height="860" viewBox="0 0 608 860" aria-label="Symptom callouts">
    <g stroke="var(--green)" stroke-width="2" fill="none">
      <line x1="418" y1="251" x2="332" y2="268"/>
      <line x1="418" y1="295" x2="338" y2="302"/>
      <line x1="418" y1="339" x2="362" y2="330"/>
      <line x1="418" y1="383" x2="382" y2="382"/>
      <line x1="418" y1="427" x2="388" y2="440"/>
      <line x1="418" y1="471" x2="318" y2="424"/>
    </g>
    <g fill="var(--green)">
      <rect x="418" y="236" width="166" height="30" rx="12"/>
      <rect x="418" y="280" width="166" height="30" rx="12"/>
      <rect x="418" y="324" width="166" height="30" rx="12"/>
      <rect x="418" y="368" width="166" height="30" rx="12"/>
      <rect x="418" y="412" width="166" height="30" rx="12"/>
      <rect x="418" y="456" width="166" height="30" rx="12"/>
    </g>
    <g fill="#fff" font-family="Open Sans, sans-serif" font-size="14" text-anchor="middle" style="font-stretch:80%">
      <text x="501" y="256">HEADACHES</text>
      <text x="501" y="300">NECK PAIN</text>
      <text x="501" y="344">SHOULDER PAIN</text>
      <text x="501" y="388">BACK PAIN</text>
      <text x="501" y="432">SCIATICA</text>
      <text x="501" y="476">ARM &amp; HAND PAIN</text>
    </g>
  </svg>

  <p class="chart-caption">AS THE HEAD TILTS FORWARD<br>MORE FORCE IS PLACED<br>ON THE SPINE</p>

  <svg class="layer" width="608" height="860" viewBox="0 0 608 860" aria-label="Bar chart of spine pressure by head tilt">
    <rect x="56" y="528" width="32" height="52" fill="var(--green)"/>
    <rect x="96" y="464" width="32" height="116" fill="var(--bar-blue)"/>
    <rect x="136" y="408" width="32" height="172" fill="var(--purple)"/>
    <rect x="176" y="369" width="32" height="211" fill="var(--rose)"/>
    <rect x="216" y="322" width="32" height="258" fill="var(--red)"/>
    <g fill="#fff" font-family="Open Sans, sans-serif" font-size="15" text-anchor="middle">
      <text x="72" y="570">12</text>
      <text x="112" y="510">27</text>
      <text x="152" y="454">40</text>
      <text x="192" y="415">49</text>
      <text x="232" y="368">60</text>
    </g>
    <g fill="var(--ink)" font-family="Open Sans, sans-serif" font-size="13" font-weight="600" text-anchor="middle">
      <text x="72" y="596">0°</text>
      <text x="112" y="596">15°</text>
      <text x="152" y="596">30°</text>
      <text x="192" y="596">45°</text>
      <text x="232" y="596">60°</text>
    </g>
  </svg>
  <p class="axis-x">DEGREES OF FORWARD HEAD TILT</p>
  <p class="axis-y">PRESSURE ON SPINE (LBS)</p>

  <div class="care">
    <div class="care-head">CHIROPRACTIC CARE</div>
    CAN HELP CORRECT AND PREVENT THESE PROBLEMS BY RESTORING AND MAINTAINING
    <span class="care-foot">PROPER ALIGNMENT OF THE NECK</span>
  </div>

  <div class="usage">
    THE AVERAGE PERSON SPENDS<br>
    <span class="usage-em">8-11 HOURS PER DAY</span><br>
    USING ELECTRONIC DEVICES
  </div>

  <svg class="layer" width="608" height="860" viewBox="0 0 608 860" aria-label="Pie chart of daily device use">
    <circle cx="100" cy="772" r="36" fill="var(--blue)"/>
    <path d="M100,772 L100,736 A36,36 0 0 1 126,797 Z" fill="var(--green)"/>
  </svg>

  <div class="offer"><span class="offer-big">50%</span><span class="offer-small">off initial consultation</span></div>
  <p class="booking">if you book online at<br><span class="booking-url">www.spineeaseclinic.com.au</span><br>choose “TECH NECK” option</p>
</main>
</body>
</html>
```